Business cards for law firm with global theme

I'd like business cards with contact info for two offices. They should include the colors and font of the new logo design, which is a stylized globe with an "F" in it. The feel should be very modern and professional.

```html
<!DOCTYPE html>
<html lang="en">
<head>
<meta charset="utf-8">
<title>Veranti Law — Business Cards</title>
<link rel="stylesheet" href="https://fonts.googleapis.com/css2?family=Montserrat:wght@400;700&family=Oswald:wght@600&display=swap">
<style>
  :root {
    --backdrop: #2a2a2a;
    --navy: #0d4e8c;
    --navy-deep: #0a3f73;
    --sky: #1fa8e6;
    --ink: #444a50;
    --paper: #ffffff;
  }
  * { box-sizing: border-box; margin: 0; padding: 0; }
  html, body { width: 1200px; height: 881px; overflow: hidden; }
  body {
    background: var(--backdrop);
    display: flex;
    align-items: center;
    justify-content: center;
    gap: 40px;
    font-family: "Montserrat", sans-serif;
  }
  .card {
    width: 540px;
    height: 309px;
    border-radius: 12px;
    position: relative;
    overflow: hidden;
    box-shadow: 0 10px 30px rgba(0,0,0,.5);
  }
  /* Back side */
  .card--back { background: var(--navy); }
  .card--back .pattern-area {
    position: absolute; inset: 0;
    background: linear-gradient(135deg, var(--navy) 0%, var(--navy-deep) 100%);
  }
  .card--back .brand {
    position: absolute; inset: 0;
    display: flex; align-items: center; justify-content: center; gap: 10px;
  }
  .brand-dot {
    width: 30px; height: 30px; border-radius: 50%;
    background: var(--sky);
  }
  .card--back .brand-name {
    color: var(--paper);
    font-weight: 700; font-size: 18px; letter-spacing: 1px;
  }
  /* Front side */
  .card--front { background: var(--paper); }
  .card--front .brand {
    position: absolute; top: 58px; left: 0; right: 0;
    display: flex; align-items: center; justify-content: center; gap: 16px;
  }
  .card--front .brand-dot { width: 62px; height: 62px; }
  .card--front .brand-name {
    color: var(--navy);
    font-weight: 700; font-size: 30px; letter-spacing: 1px;
    padding-bottom: 6px;
    border-bottom: 1.5px solid var(--sky);
  }
  .details {
    position: absolute; top: 178px; left: 0; right: 0;
    display: flex; justify-content: center; align-items: center; gap: 22px;
  }
  .person { text-align: right; }
  .person-name {
    font-family: "Oswald", sans-serif;
    font-weight: 600; font-size: 34px; color: var(--sky);
    letter-spacing: 1px; line-height: 1;
  }
  .person-title {
    font-size: 14px; color: var(--ink); letter-spacing: 1.5px; margin-top: 4px;
  }
  .divider { width: 1.5px; height: 66px; background: var(--sky); }
  .contact-list { list-style: none; font-size: 13px; color: var(--ink); }
  .contact-list li { display: flex; align-items: center; gap: 8px; line-height: 21px; }
  .contact-list svg { width: 11px; height: 11px; flex: none; }
</style>
</head>
<body>
  <section class="card card--back" aria-label="Card back">
    <div class="pattern-area" role="img" aria-label="Repeating subtle brand pattern in deep blue"></div>
    <div class="brand">
      <span class="brand-dot"></span>
      <span class="brand-name">VERANTI LAW</span>
    </div>
  </section>

  <section class="card card--front" aria-label="Card front">
    <div class="brand">
      <span class="brand-dot"></span>
      <span class="brand-name">VERANTI LAW</span>
    </div>
    <div class="details">
      <div class="person">
        <p class="person-name">DANIEL MARSH</p>
        <p class="person-title">DIRECTOR</p>
      </div>
      <span class="divider"></span>
      <ul class="contact-list">
        <li>
          <svg viewBox="0 0 12 12"><path d="M2.5 1 4.5 1 5.2 3.6 4 4.6C4.6 6 6 7.4 7.4 8L8.4 6.8 11 7.5V9.5C11 10.3 10.3 11 9.5 11 5 11 1 7 1 2.5 1 1.7 1.7 1 2.5 1Z" fill="var(--sky)"/></svg>
          201 555-0148
        </li>
        <li>
          <svg viewBox="0 0 12 12"><rect x="1" y="2.5" width="10" height="7" fill="none" stroke="var(--sky)" stroke-width="1.2"/><path d="M1 2.5 6 6.5 11 2.5" fill="none" stroke="var(--sky)" stroke-width="1.2"/></svg>
          info@verantilaw.com
        </li>
        <li>
          <svg viewBox="0 0 12 12"><circle cx="6" cy="6" r="5" fill="none" stroke="var(--sky)" stroke-width="1.1"/><path d="M1 6H11M6 1C3.5 3.5 3.5 8.5 6 11M6 1C8.5 3.5 8.5 8.5 6 11" fill="none" stroke="var(--sky)" stroke-width="1"/></svg>
          www.verantilaw.com
        </li>
      </ul>
    </div>
  </section>
</body>
</html>
```